Bright Harbor Health (03)

We're designing a website to sell Medicare Supplements. Attached is the script we want to say and general layout, but please use your best knowledge to make it better. This platform should be extremely user-friendly, but we want to make it look fun and approachable! Most Insurance/medicare websites are very boring, drab, simple but we want this one to be more personalized, fun and sexy (but again, still user-friendly since our target demographic is 65+).

This homepage should include a fun and inviting quiz, the script is in the attachment below. It should also include the blurbs about what medicare supplements plans are and why they should buy them. Feel free to play around with cool fonts and imagery, we want the site to be engaging!

Target Market(s)

seniors

Industry/Entity Type

Insurance

Number of Pages Required

1 page

Requirements
Must have
• Quiz, company name and tag line, script
Nice to have
• fun, engaging elements

```html
<!DOCTYPE html>
<html lang="en">
<head>
<meta charset="utf-8">
<title>Bright Harbor Health – Medicare Supplements</title>
<link href="https://fonts.googleapis.com/css2?family=Arima:wght@400;500;600;700&family=Ubuntu:wght@500&display=swap" rel="stylesheet">
<style>
:root{
  --navy:#2c3459;
  --lime:#94d340;
  --lime-soft:rgba(160,220,80,.82);
  --red:#b81515;
  --grey-bg:#f3f3f3;
  --ink:#1e1e1e;
  --white:#ffffff;
  --pink:#e63cc8;
}
*{margin:0;padding:0;box-sizing:border-box}
html,body{width:1200px;height:2183px;overflow:hidden}
body{position:relative;font-family:"Arima",serif;background:var(--white);color:var(--ink)}
.abs{position:absolute}

/* hero */
.hero{left:0;top:0;width:1200px;height:596px;background:linear-gradient(100deg,#6b5a4c 0%,#8f7a62 30%,#b9a27f 55%,#7a6a58 80%,#4d4540 100%)}
.hero-band{left:0;top:197px;width:1200px;height:263px;background:linear-gradient(90deg,var(--lime-soft) 0%,var(--lime-soft) 62%,rgba(160,220,80,0) 78%)}
.topbar{left:0;top:0;width:1200px;height:97px;background:rgba(40,40,48,.72)}
.brand{left:112px;top:26px;font-size:30px;font-weight:700;color:var(--white)}
.nav{top:36px;font-family:"Ubuntu",sans-serif;font-size:17px;color:var(--white)}
.nav.active::after{content:"";position:absolute;left:-10px;right:-12px;top:26px;height:3px;background:var(--lime);border-radius:2px}
.account{left:950px;top:40px;font-family:"Ubuntu",sans-serif;font-size:14px;color:var(--white);display:flex;align-items:center;gap:6px}
.account .bar{color:var(--lime)}
.hero-title{left:112px;top:226px;font-size:43px;font-weight:700;color:var(--navy);letter-spacing:.5px}
.hero-sub{left:113px;top:290px;font-size:26px;font-weight:500;line-height:35px;color:var(--white)}
.hero-dial{left:113px;top:382px;font-size:31px;font-weight:600;color:var(--red)}
.hero-dial span{font-size:22px;color:var(--navy);font-weight:500}

/* intro */
.intro{left:112px;top:650px;width:975px;height:176px;background:var(--lime);border-radius:17px;text-align:center;padding-top:18px}
.intro p{font-size:17px;line-height:29px}
.intro strong{display:block;margin-top:10px;font-size:21px;font-weight:600;line-height:29px}

/* quiz */
.quiz{left:293px;top:871px;width:615px;height:395px;background:var(--navy);border-radius:20px;box-shadow:0 2px 6px rgba(0,0,0,.25)}
.quiz-step{left:32px;top:32px;font-size:20px;color:var(--white)}
.quiz-q{left:0;top:46px;width:615px;text-align:center;font-size:36px;font-weight:600;color:var(--lime)}
.opt-key{font-size:32px;font-weight:600;color:var(--lime);left:84px}
.opt-radio{left:131px;width:35px;height:35px;border-radius:50%;background:var(--white);border:3px solid var(--lime)}
.opt-field{left:178px;width:351px;height:37px;background:linear-gradient(#fff 60%,#e6e6e6);border-radius:6px;font-size:18px;line-height:39px;padding-left:17px;color:var(--ink)}
.quiz-btn{left:219px;top:281px;width:176px;height:44px;border-radius:22px;background:var(--lime);color:var(--navy);font-size:22px;font-weight:600;text-align:center;line-height:46px}

/* info */
.info{left:0;top:1312px;width:1200px;height:484px;background:var(--grey-bg);padding:42px 112px 0}
.info h2{font-size:18px;font-weight:500;color:var(--navy);margin-bottom:16px}
.info p{font-size:12px;line-height:17.6px;color:var(--navy)}
.info ul{list-style:none;margin:17px 0 16px 30px}
.info li{font-size:12px;line-height:17.6px;color:var(--navy);position:relative;padding-left:16px}
.info li::before{content:"";position:absolute;left:0;top:4px;width:11px;height:11px;border-radius:50%;background:var(--navy)}

/* footer */
.footer{left:0;top:1796px;width:1200px;height:387px;background:var(--navy)}
.f-brand{left:138px;top:66px;font-size:32px;font-weight:700;color:var(--lime)}
.f-about{left:138px;top:114px;width:260px;font-size:13px;line-height:22px;color:var(--lime)}
.social{top:269px;width:21px;height:21px;border-radius:50%;background:var(--lime)}
.f-head{font-size:26px;font-weight:600;color:var(--lime);letter-spacing:1.5px}
.f-links{left:568px;top:110px;list-style:none}
.f-links li{font-size:18px;line-height:31px;color:var(--lime);letter-spacing:1.5px}
.f-links li.current{color:var(--pink)}
.contact{left:836px;top:120px;list-style:none;color:var(--lime);font-size:18px;letter-spacing:1.5px}
.contact li{display:flex;align-items:flex-start;gap:10px;line-height:30px;margin-bottom:4px}
.contact svg{flex:none;margin-top:6px}
.f-rule{left:112px;top:336px;width:976px;height:1px;background:rgba(255,255,255,.45)}
.copy{left:0;top:355px;width:1200px;text-align:center;font-size:11px;color:var(--white);letter-spacing:.6px}
</style>
</head>
<body>

<div class="abs hero" role="img" aria-label="Photo of smiling senior friends sharing grapes and wine at an outdoor table"></div>
<div class="abs hero-band"></div>

<header class="abs topbar">
  <div class="abs brand">Bright Harbor Health</div>
  <div class="abs nav active" style="left:446px">Home</div>
  <div class="abs nav" style="left:539px">About Us</div>
  <div class="abs nav" style="left:659px">Learn about medicare</div>
  <div class="abs account">
    <svg width="13" height="15" viewBox="0 0 13 15"><rect x="1" y="6" width="11" height="9" rx="1.5" fill="#94d340"/><path d="M3.5 6V4.2a3 3 0 0 1 6 0V6" fill="none" stroke="#94d340" stroke-width="2"/></svg>
    <span>Login <span class="bar">|</span> Register</span>
  </div>
</header>

<h1 class="abs hero-title">Welcome to Bright Harbor Health</h1>
<p class="abs hero-sub">Be confident in choosing the Medicare<br>Supplement plan that’s right for you.</p>
<p class="abs hero-dial">Dial (800) 555-0142 <span>to talk to a live agent</span></p>

<section class="abs intro">
  <p>We know insurance can be confusing. With so much information and not enough answers, we’re<br>here to help you find the plan that works best for you, your family and your health.</p>
  <strong>Take this short quiz to find flexible and<br>affordable plans that you can feel confident in.</strong>
</section>

<section class="abs quiz">
  <div class="abs quiz-step">1/4</div>
  <div class="abs quiz-q">Q1. I am</div>

  <div class="abs opt-key" style="top:108px">a :</div>
  <svg class="abs" style="left:131px;top:110px" width="42" height="42" viewBox="0 0 42 42">
    <circle cx="19" cy="22" r="17" fill="#fff" stroke="#1e1e1e" stroke-width="2"/>
    <circle cx="19" cy="22" r="12" fill="#3b8fd6"/>
    <circle cx="19" cy="22" r="8" fill="#fff"/>
    <circle cx="19" cy="22" r="4" fill="#3b8fd6"/>
    <path d="M19 22L36 5" stroke="#1e1e1e" stroke-width="2"/>
    <path d="M33 4l5-1-1 5" fill="none" stroke="#94d340" stroke-width="2"/>
  </svg>
  <div class="abs opt-field" style="top:111px">Over 64 years old</div>

  <div class="abs opt-key" style="top:162px">b :</div>
  <div class="abs opt-radio" style="top:165px"></div>
  <div class="abs opt-field" style="top:165px">64 years old</div>

  <div class="abs opt-key" style="top:216px">c :</div>
  <div class="abs opt-radio" style="top:219px"></div>
  <div class="abs opt-field" style="top:219px">Under 64 years old</div>

  <div class="abs quiz-btn">Next Question</div>
</section>

<section class="abs info">
  <h2>What is a Medicare Supplement plan?</h2>
  <p>Each Medicare Supplement insurance plan offers a different level of basic benefits, but each lettered plan will include the same standardized basic benefits regardless of insurance company and location. Medicare Supplement insurance plans do not always cover vision, dental, long-term care, or hearing aids, but all plans must cover at least a portion of the following basic benefits:</p>
  <ul>
    <li>Medicare Part A coinsurance costs up to an additional 365 days after Medicare benefits are exhausted</li>
    <li>Medicare Part A hospice care coinsurance or copayments</li>
    <li>Medicare Part B coinsurance or copayments</li>
    <li>First three pints of blood used in a medical procedure</li>
  </ul>
  <h2>Medicare Supplement insurance plan costs</h2>
  <p>Although private insurance companies are required to offer the same basic benefits for each lettered plan, they do have the ability to charge different premiums. You might want to shop around to find a Medicare Supplement insurance plan that may fit your medical and financial needs. Insurance companies may price their plan premiums in any of the following ways:</p>
  <ul>
    <li>Community no-age-rated: These Medicare Supplement insurance plans charge premiums that are the same across the board, regardless of age.</li>
    <li>Issue-age-rated: These plans base their premiums on your age when you first enrolled in the policy. Therefore, the younger you are when you enroll in this type of plan, the lower your premium will be.</li>
    <li>Attained-age-rated: Like issue-age-rated, these plans base their premiums on the age you were when you first bought a policy, but unlike issue-age-rated, premiums increase as you get older. Please note that no matter what rating method an insurance company uses, premiums may increase over time for reasons other than age, such as inflation.</li>
  </ul>
</section>

<footer class="abs footer">
  <div class="abs f-brand">Bright Harbor Health</div>
  <p class="abs f-about">Lorem ipsum dolor sit amet, conse ctetur adipiscing elit, sed do eiusmod tempor incididunt ut labore et dolore magna aliqua. Quis ipsum suspendisse ultrices gravida. Risus commodo vive rra maecenas accumsan lacus vel facilisis.</p>
  <span class="abs social" style="left:138px" aria-label="Social profile"></span>
  <span class="abs social" style="left:186px" aria-label="Social profile"></span>
  <span class="abs social" style="left:232px" aria-label="Social profile"></span>
  <span class="abs social" style="left:277px" aria-label="Social profile"></span>

  <div class="abs f-head" style="left:574px;top:52px">Link</div>
  <ul class="abs f-links">
    <li class="current">About</li>
    <li>Blog</li>
    <li>Privecy Policy</li>
    <li>Terms</li>
    <li>Cokies</li>
    <li>Site map</li>
  </ul>

  <div class="abs f-head" style="left:858px;top:64px">Contact Us</div>
  <ul class="abs contact">
    <li><svg width="16" height="16" viewBox="0 0 16 16"><rect width="16" height="16" rx="2" fill="#94d340"/><path d="M5 3.5l2 2-1 1.3c.6 1.3 1.6 2.3 2.9 2.9l1.3-1 2 2-1.2 1.6C7.6 12 4 8.4 3.7 4.7z" fill="#2c3459"/></svg>(800) 555-0142</li>
    <li><svg width="20" height="16" viewBox="0 0 20 16"><rect x="1" y="2" width="18" height="12" rx="1.5" fill="#94d340"/><path d="M1.5 3l8.5 6 8.5-6" fill="none" stroke="#2c3459" stroke-width="1.6"/></svg>hello@brightharbor.example</li>
    <li><svg width="18" height="18" viewBox="0 0 18 18"><path d="M17 1L1 8l7 2 2 7z" fill="#94d340"/></svg>14 Lantern Bay Road,<br>Milford, CA,<br>10005</li>
  </ul>

  <div class="abs f-rule"></div>
  <p class="abs copy">© 2020 Brightharborhealth.example. All Rights reserved</p>
</footer>

</body>
</html>
```